BRAVOK PRESSURE WASHING LLC

am starting a small pressure washing business in myrtle beach. I need a weebsite that will get people attention. I wanrto advertise our services . Main two : We specialize in roof cleaning , window cleaning . Other services are : residential and commercial, driveways & sidewalks, gutter cleaning, patio & deck cleaning, curb appeal, heavy equipment, mobile homes, car lots, fleets, store fronts, commercial buildings, grocery kart sanitizing, have a couple phrases saying. " Make your home shine" " Make your home look new again" I need a section showing our work in the past. Im going to send you some ,before and after pictures of our work. Also put the 100% satisfaction guaranteed ribbon somewhere on the website and give us a call for your free estiment 843 555 0176. Licensed and insured. Also need a page listing our services and a paragraph or two of the importance of that service. Maybe a section where customers can comment and give good reviews. I need it to have my logo and make it look modern and catch the eye . We founded in 2019 and use environmental amd pet friendly chemicals and top of the line pressure washing equipment. Thank you.l

```html
<!DOCTYPE html>
<html lang="en">
<head>
<meta charset="utf-8">
<title>Bravok Pressure Washing LLC</title>
<link href="https://fonts.googleapis.com/css2?family=Lato:ital,wght@0,400;0,700;1,400&family=Nunito+Sans:wght@700;800;900&display=swap" rel="stylesheet">
<style>
:root{
  --orange:#f7a21b;
  --blue:#1a73d0;
  --blue-deep:#0f4f9e;
  --navy:#1b3a66;
  --sky:#5aaee6;
  --ink:#2b2b2b;
  --muted:#6b6b6b;
  --white:#ffffff;
  --footer:#1f2a22;
}
*{box-sizing:border-box;margin:0;padding:0}
html,body{width:1200px;height:3899px;overflow:hidden;background:var(--white)}
body{position:relative;font-family:"Lato",sans-serif;color:var(--ink)}
.fill{position:absolute;z-index:0}
.curves{position:absolute;left:0;top:0;z-index:1;pointer-events:none}
.layer{position:absolute;z-index:2}
h1,h2,h3{font-family:"Nunito Sans",sans-serif;font-weight:800}
.btn{position:absolute;z-index:2;display:flex;align-items:center;justify-content:center;background:var(--orange);color:var(--white);font-family:"Nunito Sans",sans-serif;font-weight:800;border-radius:40px;font-size:17px;letter-spacing:.3px}

/* header */
.brand{left:110px;top:14px;color:var(--blue-deep);font-family:"Nunito Sans",sans-serif;font-weight:900;line-height:1;white-space:nowrap}
.brand .name{font-size:44px;letter-spacing:1px}
.brand .sub{font-size:12px;margin-top:6px;letter-spacing:.6px}
.call{right:110px;top:22px;font-size:18px;color:var(--ink);display:flex;align-items:center;gap:8px;white-space:nowrap}
.call strong{color:var(--blue);font-size:22px;font-weight:700}
.nav{right:112px;top:76px;display:flex;gap:38px;font-size:17px;font-weight:700;color:var(--ink);white-space:nowrap}
.nav .active{color:var(--orange)}

/* hero */
.hero-photo{left:0;top:115px;width:1200px;height:610px;background:linear-gradient(180deg,#1683c9 0%,#3aa0dc 40%,#9c8a6c 70%,#c9b79a 100%)}
.hero-title{left:0;top:185px;width:1200px;text-align:center;color:var(--white);font-size:53px;font-weight:800}
.dots{left:558px;top:614px;display:flex;gap:8px}
.dots span{width:15px;height:15px;border-radius:50%;border:2px solid var(--white)}
.dots span:first-child{background:var(--white)}

/* welcome */
.welcome-title{left:111px;top:762px;width:520px;font-size:34px;line-height:51px;color:#222;white-space:nowrap}
.welcome-text{left:111px;top:880px;width:480px;font-size:16.5px;line-height:31px;color:var(--muted)}
.welcome-text p+p{margin-top:31px}
.video{left:646px;top:772px;width:442px;height:264px;background:linear-gradient(135deg,#6b2c20 0%,#9a5a44 35%,#d8d8d8 70%,#a9b4bd 100%);box-shadow:0 6px 18px rgba(0,0,0,.25)}
.play{left:834px;top:872px;width:66px;height:66px;border-radius:50%;background:rgba(0,0,0,.75)}

/* services */
.svc-photo-l{left:0;top:1188px;width:600px;height:612px;background:linear-gradient(160deg,#33506f,#5a7088 60%,#3b4f3a)}
.svc-photo-r{left:600px;top:1188px;width:600px;height:612px;background:linear-gradient(160deg,#9cc7e5,#cfe5f2 55%,#6f9a6b)}
.panel-l{left:0;top:1240px;width:592px;height:490px;background:rgba(18,58,116,.86)}
.panel-r{left:607px;top:1240px;width:593px;height:490px;background:rgba(74,160,222,.82)}
.svc{color:var(--white)}
.svc .icon{width:128px;height:128px;border-radius:50%;border:3px solid var(--white);display:flex;align-items:center;justify-content:center}
.svc h2{font-size:36px;margin-top:20px;line-height:44px;white-space:nowrap}
.svc p{font-size:16.5px;line-height:31px;margin-top:14px;width:440px}

/* projects */
.section-title{left:0;width:1200px;text-align:center;font-size:36px;color:#222}
.proj{position:absolute;z-index:2;background:#888}
.arrow{position:absolute;z-index:3;width:40px;height:40px;border-radius:50%;background:var(--white);display:flex;align-items:center;justify-content:center;box-shadow:0 1px 4px rgba(0,0,0,.3)}

/* satisfaction */
.sat-band{left:0;top:2391px;width:1200px;height:393px;background:radial-gradient(circle at 75% 50%,#2b86e0,#1466c8 60%,#0f5bb8)}
.sat-title{left:110px;top:2510px;font-size:56px;line-height:78px;color:var(--white);font-weight:900;white-space:nowrap}
.worker{left:800px;top:2462px;width:330px;height:300px;border-radius:50%;background:radial-gradient(circle at 50% 45%,#f7a21b 0%,#f7a21b 55%,#1d3f86 56%,#1d3f86 100%)}

/* reviews */
.avatar{left:514px;top:2854px;width:172px;height:172px;border-radius:50%;background:#d9d9d9;border:7px solid #f4f4f4;box-shadow:0 2px 10px rgba(0,0,0,.2)}
.quote{left:230px;top:3052px;width:740px;text-align:center;font-style:italic;font-size:16.5px;line-height:31px;color:var(--muted)}
.reviewer{left:0;top:3168px;width:1200px;text-align:center;font-size:17px;color:#444}

/* footer */
.footer-photo{left:0;top:3250px;width:1200px;height:649px;background:linear-gradient(180deg,#2c3b2c 0%,#1d261f 60%,#121812 100%)}
.contact-title{top:3355px;color:var(--white)}
.form-title,.info-title{font-family:"Lato",sans-serif;font-weight:700;font-size:22px;color:var(--white)}
.field{position:absolute;z-index:2;background:var(--white);border-radius:4px;font-size:15px;color:#777;padding:11px 15px}
.info{left:778px;top:3500px;color:var(--white);font-size:16.5px}
.info .row{position:absolute;left:0;display:flex;align-items:center;gap:16px;width:340px;white-space:nowrap}
.info .ic{width:34px;height:34px;border-radius:50%;border:1.5px solid rgba(255,255,255,.7);display:flex;align-items:center;justify-content:center;flex:none}
.rule{left:112px;top:3812px;width:968px;height:1px;background:rgba(255,255,255,.35)}
.copy{left:112px;top:3843px;font-size:16px;color:var(--white);white-space:nowrap}
.social{position:absolute;z-index:2;width:36px;height:36px;border-radius:50%;border:1.5px solid var(--white);display:flex;align-items:center;justify-content:center}
.social span{width:12px;height:12px;border-radius:50%;background:var(--white)}
</style>
</head>
<body>

<div class="fill hero-photo" role="img" aria-label="Photo of a row of stone and siding houses under a blue sky"></div>
<div class="fill svc-photo-l" role="img" aria-label="Photo of a worker cleaning a roof"></div>
<div class="fill svc-photo-r" role="img" aria-label="Photo of clean house windows"></div>
<div class="fill sat-band"></div>
<div class="fill footer-photo" role="img" aria-label="Dark photo of a person pressure washing a path"></div>

<svg class="curves" width="1200" height="3899" viewBox="0 0 1200 3899" aria-hidden="true">
  <path d="M0,598 C360,735 820,725 1200,582 L1200,640 C820,742 360,748 0,615 Z" fill="var(--orange)"/>
  <path d="M0,606 C360,728 820,718 1200,618 L1200,740 L0,740 Z" fill="var(--white)"/>
  <path d="M0,1180 L0,1190 C300,1262 900,1262 1200,1188 L1200,1180 Z" fill="var(--white)"/>
  <path d="M0,1802 C300,1700 900,1700 1200,1802 L1200,1815 L0,1815 Z" fill="var(--white)"/>
  <path d="M0,2385 L0,2392 C300,2462 900,2462 1200,2392 L1200,2385 Z" fill="var(--white)"/>
  <path d="M0,2786 C320,2690 880,2690 1200,2786 L1200,2795 L0,2795 Z" fill="var(--white)"/>
  <path d="M0,3382 C320,3230 880,3230 1200,3400 L1200,3420 C880,3258 320,3258 0,3405 Z" fill="var(--orange)"/>
  <path d="M0,3245 L0,3385 C320,3236 880,3236 1200,3390 L1200,3245 Z" fill="var(--white)"/>
</svg>

<!-- header -->
<div class="layer brand"><div class="name">BRAVOK</div><div class="sub">PRESSURE WASHING LLC</div></div>
<div class="layer call">
  <svg width="14" height="14" viewBox="0 0 24 24"><path fill="var(--orange)" d="M6.6 10.8c1.4 2.8 3.8 5.1 6.6 6.6l2.2-2.2c.3-.3.7-.4 1-.2 1.1.4 2.3.6 3.6.6.6 0 1 .4 1 1V20c0 .6-.4 1-1 1C10.6 21 3 13.4 3 4c0-.6.4-1 1-1h3.5c.6 0 1 .4 1 1 0 1.3.2 2.5.6 3.6.1.3 0 .7-.2 1z"/></svg>
  Call For Your Free Estiment <strong>843 555 0176</strong>
</div>
<nav class="layer nav"><span class="active">HOME</span><span>ABOUT US</span><span>SERVICES</span><span>PROJECTS</span><span>CONTACT US</span></nav>

<!-- hero -->
<h1 class="layer hero-title">Make Your Home Look New Again</h1>
<div class="btn" style="left:495px;top:281px;width:212px;height:64px;font-size:21px">GET A QUOTE</div>
<div class="layer dots"><span></span><span></span><span></span><span></span></div>

<!-- welcome -->
<h2 class="layer welcome-title">WELCOME TO<br>BRAVOK PRESSURE WASHING</h2>
<div class="layer welcome-text">
  <p>Nemo enim ipsam voluptatem quia voluptas sit aspernatur aut odit aut fugit, sed quia consequ.</p>
  <p>Ntur magni dolores eos qui rati one voluptatem sequi nesciunt. Neque porro quisquam est, qui d olorem ipsum quia dolor sit amet, consectetur, adipisci velit, sed qu.</p>
</div>
<div class="btn" style="left:112px;top:1098px;width:169px;height:59px">READ MORE</div>
<div class="layer video" role="img" aria-label="Video still of a brick storefront with clean windows"></div>
<div class="layer play"></div>
<svg class="layer" style="left:857px;top:890px" width="28" height="30" viewBox="0 0 28 30"><path d="M2,1 L26,15 L2,29 Z" fill="var(--white)"/></svg>

<!-- services -->
<div class="fill panel-l" style="z-index:1"></div>
<div class="fill panel-r" style="z-index:1"></div>
<div class="layer svc" style="left:100px;top:1283px">
  <div class="icon"><svg width="70" height="60" viewBox="0 0 70 60" fill="none" stroke="#fff" stroke-width="3"><rect x="8" y="28" width="40" height="26"/><path d="M8,37 H48 M8,46 H48 M18,28 V54 M28,28 V54 M38,28 V54 M30,18 H58 M44,10 V18"/><path d="M58,6 l2,5 5,2 -5,2 -2,5 -2,-5 -5,-2 5,-2z"/></svg></div>
  <h2 style="margin-left:10px">ROOF CLEANING</h2>
  <p style="margin-left:12px">Ut enim ad minima veniam, quis nostrum exercitationem ullam corporis suscipit laboriosam, nisi ut aliquid ex ea commodi consequa voluptat.</p>
</div>
<div class="btn" style="left:112px;top:1625px;width:169px;height:58px">READ MORE</div>
<div class="layer svc" style="left:652px;top:1283px">
  <div class="icon"><svg width="70" height="66" viewBox="0 0 70 66" fill="none" stroke="#fff" stroke-width="3"><rect x="8" y="6" width="54" height="54"/><path d="M35,6 V60 M8,56 H62"/><path d="M16,16 l6,-6 M16,24 l10,-10"/><path d="M48,22 l2,4 4,2 -4,2 -2,4 -2,-4 -4,-2 4,-2z M18,40 l1.5,3 3,1.5 -3,1.5 -1.5,3 -1.5,-3 -3,-1.5 3,-1.5z"/></svg></div>
  <h2 style="margin-left:10px">WINDOW CLEANING</h2>
  <p style="margin-left:12px">Ut enim ad minima veniam, quis nostrum exercitationem ullam corporis suscipit laboriosam, nisi ut aliquid ex ea commodi consequa voluptat.</p>
</div>
<div class="btn" style="left:666px;top:1625px;width:169px;height:58px">READ MORE</div>

<!-- projects -->
<h2 class="layer section-title" style="top:1790px">OUR PROJECTS</h2>
<div class="proj" style="left:112px;top:1876px;width:275px;height:209px;background:linear-gradient(160deg,#4b4b4b,#9a9a9a 60%,#c8c8c8)" role="img" aria-label="Before photo of a dirty concrete patio"></div>
<div class="proj" style="left:112px;top:2092px;width:275px;height:208px;background:linear-gradient(160deg,#7a3a2c,#9a6a58 50%,#b9b2a8)" role="img" aria-label="After photo of a clean brick porch and patio"></div>
<div class="proj" style="left:396px;top:1876px;width:407px;height:209px;background:linear-gradient(90deg,#8d8f8a 0%,#a5a7a2 50%,#5d605c 50.5%,#c4c6c2 100%)" role="img" aria-label="Before and after photo of house siding"></div>
<div class="proj" style="left:396px;top:2092px;width:407px;height:208px;background:linear-gradient(90deg,#6e7166 0%,#55704a 50%,#5e5e58 50.5%,#4f7a3c 100%)" role="img" aria-label="Before and after photo of a cleaned house roof"></div>
<div class="proj" style="left:811px;top:1876px;width:277px;height:209px;background:linear-gradient(180deg,#3e6a34,#8aa576 55%,#c9c6bc)" role="img" aria-label="Before photo of a stained driveway"></div>
<div class="proj" style="left:811px;top:2092px;width:277px;height:208px;background:linear-gradient(180deg,#5b6560,#a3ab9d 45%,#d6d6d2)" role="img" aria-label="After photo of a clean driveway"></div>
<div class="arrow" style="left:230px;top:2067px"><svg width="16" height="10" viewBox="0 0 16 10"><path d="M1,1 L8,8 L15,1" stroke="#222" stroke-width="2" fill="none"/></svg></div>
<div class="arrow" style="left:580px;top:1961px"><svg width="10" height="16" viewBox="0 0 10 16"><path d="M1,1 L8,8 L1,15" stroke="#222" stroke-width="2" fill="none"/></svg></div>
<div class="arrow" style="left:580px;top:2176px"><svg width="10" height="16" viewBox="0 0 10 16"><path d="M1,1 L8,8 L1,15" stroke="#222" stroke-width="2" fill="none"/></svg></div>
<div class="arrow" style="left:930px;top:2069px"><svg width="16" height="10" viewBox="0 0 16 10"><path d="M1,1 L8,8 L15,1" stroke="#222" stroke-width="2" fill="none"/></svg></div>
<div class="btn" style="left:516px;top:2345px;width:168px;height:58px">VIEW MORE</div>

<!-- satisfaction -->
<h2 class="layer sat-title">100% SATISFACTION<br>GUARANTEED</h2>
<div class="layer worker" role="img" aria-label="Illustration of a pressure washing worker holding a spray wand"></div>

<!-- reviews -->
<h2 class="layer section-title" style="top:2775px">CLIENT REVIEWS</h2>
<div class="layer avatar" role="img" aria-label="Reviewer avatar placeholder"></div>
<svg class="layer" style="left:96px;top:2984px" width="24" height="40" viewBox="0 0 24 40"><path d="M20,3 L4,20 L20,37" stroke="#555" stroke-width="3" fill="none"/></svg>
<svg class="layer" style="left:1076px;top:2984px" width="24" height="40" viewBox="0 0 24 40"><path d="M4,3 L20,20 L4,37" stroke="#555" stroke-width="3" fill="none"/></svg>
<p class="layer quote">“ Nemo enim ipsam voluptatem quia voluptas sit aspernatur aut odit aut fugit, sed quia cons equuntur magni dolores eos qui ratione voluptatem sequi nesciunt. Neque porro quisquam est, qui dolorem ipsum quia dolor sit amet, consectetur, adipisci veli. ”</p>
<p class="layer reviewer">- MARA</p>

<!-- contact -->
<h2 class="layer section-title contact-title">CONTACT US</h2>
<h3 class="layer form-title" style="left:110px;top:3450px">Request a Quote</h3>
<div class="field" style="left:112px;top:3510px;width:296px;height:44px">Name :</div>
<div class="field" style="left:418px;top:3510px;width:296px;height:44px">Phone no :</div>
<div class="field" style="left:112px;top:3571px;width:602px;height:44px">Email :</div>
<div class="field" style="left:112px;top:3633px;width:602px;height:81px">Message :</div>
<div class="btn" style="left:584px;top:3730px;width:130px;height:48px;font-size:19px">SUBMIT</div>

<h3 class="layer info-title" style="left:778px;top:3450px">Contact Information</h3>
<div class="layer info">
  <div class="row" style="top:0"><span class="ic"><svg width="12" height="16" viewBox="0 0 12 16"><path d="M6,0 C2.7,0 0,2.6 0,5.8 C0,10 6,16 6,16 S12,10 12,5.8 C12,2.6 9.3,0 6,0 Z M6,8 A2.2,2.2 0 1 1 6,3.6 A2.2,2.2 0 0 1 6,8 Z" fill="#fff"/></svg></span><span style="line-height:22px">410 Coastal Palm Ave Suite 2<br>Myrtle Beach, SC 29577</span></div>
  <div class="row" style="top:72px"><span class="ic"><svg width="14" height="14" viewBox="0 0 24 24"><path fill="#fff" d="M6.6 10.8c1.4 2.8 3.8 5.1 6.6 6.6l2.2-2.2c.3-.3.7-.4 1-.2 1.1.4 2.3.6 3.6.6.6 0 1 .4 1 1V20c0 .6-.4 1-1 1C10.6 21 3 13.4 3 4c0-.6.4-1 1-1h3.5c.6 0 1 .4 1 1 0 1.3.2 2.5.6 3.6.1.3 0 .7-.2 1z"/></svg></span>1 843 555 0188</div>
  <div class="row" style="top:133px"><span class="ic"><svg width="14" height="14" viewBox="0 0 14 14"><rect x="1" y="5" width="12" height="8" rx="1" fill="#fff"/><rect x="3.5" y="1" width="7" height="4" fill="none" stroke="#fff" stroke-width="1.5"/></svg></span>1 843 555 0199</div>
  <div class="row" style="top:190px"><span class="ic"><svg width="14" height="11" viewBox="0 0 14 11"><rect x="0" y="0" width="14" height="11" rx="1" fill="#fff"/><path d="M1,1 L7,6 L13,1" stroke="#1f2a22" stroke-width="1.4" fill="none"/></svg></span>info@bravokwash.com</div>
</div>

<div class="layer rule"></div>
<p class="layer copy">Copyright © 2020, BRAVOK PRESSURE WASHING. All rights reserved.</p>
<div class="social" style="left:950px;top:3837px"><span></span></div>
<div class="social" style="left:997px;top:3837px"><span></span></div>
<div class="social" style="left:1044px;top:3837px"><span></span></div>
<svg class="layer" style="left:1133px;top:3845px" width="28" height="16" viewBox="0 0 28 16"><path d="M2,14 L14,3 L26,14" stroke="#fff" stroke-width="3" fill="none"/></svg>

</body>
</html>
```